Calvanta Group Real Estate Company business cards

New business card design, we are generally happy with the basic layout of the existing front of business card, (feel free to change) but require a head shot photo on the back side.

http://www.calvanta.com.au/

Attached logos, and existing business card

------------------------------

Target Market(s)

Real estate

Industry/Entity Type

Real Estate

Contact Information for Business Card

Standard size double sided

Font styles to use
Other font styles liked:
• Futura

Requirements
Must have
• Photo head shot on the back side
Nice to have
• yes
Should not have
• No

```html
<!DOCTYPE html>
<html lang="en">
<head>
<meta charset="utf-8">
<title>Calvanta Group – Business Card</title>
<link rel="stylesheet" href="https://fonts.googleapis.com/css2?family=Open+Sans:wght@400;600;700&display=swap">
<style>
  :root {
    --page-bg: #2e2824;
    --card-bg: #0d0d0d;
    --card-edge: #1c1c1c;
    --brand-purple: #3a2f7a;
    --accent-orange: #f39a1e;
    --text-white: #f2f2f2;
    --photo-light: #e9e9e9;
    --photo-mid: #b9b9b9;
  }
  * { box-sizing: border-box; margin: 0; padding: 0; }
  html, body { width: 1200px; height: 844px; overflow: hidden; }
  body {
    background: var(--page-bg);
    font-family: "Open Sans", Arial, sans-serif;
    display: flex;
    align-items: center;
    justify-content: center;
    gap: 40px;
  }
  .card {
    position: relative;
    width: 540px;
    height: 330px;
    background: var(--card-bg);
    border: 1px solid var(--card-edge);
    border-radius: 3px;
    box-shadow: 0 10px 24px rgba(0,0,0,.45);
    color: var(--text-white);
  }

  /* Front */
  .brand {
    position: absolute;
    left: 70px;
    top: 62px;
    display: flex;
    align-items: center;
    gap: 12px;
    color: var(--brand-purple);
    font-weight: 600;
    font-size: 58px;
    letter-spacing: -1px;
    line-height: 1;
  }
  .brand-square {
    width: 22px;
    height: 22px;
    background: var(--brand-purple);
  }
  .contact-list {
    position: absolute;
    right: 26px;
    top: 168px;
    list-style: none;
    text-align: right;
    font-size: 13px;
    line-height: 21px;
  }
  .contact-list li { display: flex; justify-content: flex-end; align-items: center; gap: 8px; }
  .contact-list svg { width: 11px; height: 11px; fill: var(--accent-orange); }
  .holder {
    position: absolute;
    left: 26px;
    bottom: 30px;
  }
  .holder-name { color: var(--accent-orange); font-weight: 700; font-size: 19px; }
  .holder-role { font-size: 13px; margin-top: 1px; }
  .company-name { color: var(--accent-orange); font-weight: 700; font-size: 16px; margin-top: 18px; }
  .company-abn { font-size: 14px; }
  .company-abn strong { font-weight: 700; }

  /* Back */
  .tagline {
    position: absolute;
    top: 56px;
    width: 100%;
    text-align: center;
    color: var(--accent-orange);
    font-weight: 600;
    font-size: 14px;
  }
  .headshot {
    position: absolute;
    left: 50%;
    top: 86px;
    width: 120px;
    height: 120px;
    margin-left: -60px;
    border-radius: 50%;
    background: radial-gradient(circle at 50% 45%, var(--photo-light) 0%, var(--photo-mid) 60%, rgba(13,13,13,0) 72%);
  }
  .services {
    position: absolute;
    top: 222px;
    width: 100%;
    text-align: center;
    font-weight: 600;
    font-size: 15px;
    word-spacing: 3px;
  }
  .services .divider { color: var(--accent-orange); }
</style>
</head>
<body>
  <section class="card card-front">
    <div class="brand"><span class="brand-square"></span><span>calvanta group</span></div>

    <ul class="contact-list">
      <li>0412 555 318
        <svg viewBox="0 0 24 24"><path d="M6.6 10.8a15.1 15.1 0 0 0 6.6 6.6l2.2-2.2a1 1 0 0 1 1-.25 11.4 11.4 0 0 0 3.6.57 1 1 0 0 1 1 1V20a1 1 0 0 1-1 1A17 17 0 0 1 3 4a1 1 0 0 1 1-1h3.5a1 1 0 0 1 1 1c0 1.25.2 2.45.57 3.6a1 1 0 0 1-.25 1z"/></svg>
      </li>
      <li>daniel.tran@calvanta.com.au
        <svg viewBox="0 0 24 24"><path d="M2 5h20v14H2z M3 6l9 7 9-7" fill="none" stroke="#f39a1e" stroke-width="0"/><path d="M2 5h20v2l-10 7L2 7z"/><path d="M2 9l10 7 10-7v10H2z"/></svg>
      </li>
      <li>www.calvanta.com.au
        <svg viewBox="0 0 24 24"><circle cx="12" cy="12" r="10"/><path d="M2 12h20M12 2c3 3 3 17 0 20M12 2c-3 3-3 17 0 20" stroke="#0d0d0d" stroke-width="1.5" fill="none"/></svg>
      </li>
    </ul>

    <div class="holder">
      <p class="holder-name">Daniel Tran</p>
      <p class="holder-role">Director</p>
      <p class="company-name">Calvanta Group</p>
      <p class="company-abn"><strong>ABN:</strong> 41 208 663 915</p>
    </div>
  </section>

  <section class="card card-back">
    <p class="tagline">let us show you property</p>
    <div class="headshot" role="img" aria-label="Head shot photo of the director"></div>
    <p class="services">Buy <span class="divider">|</span> Sell <span class="divider">|</span> Rent</p>
  </section>
</body>
</html>
```